Cedar Lantern Letterhead

I just need letterhead for my integrative psychiatry business. I'm going to use this to do mailings to other doctors, as well as send letters to patients. Thank you

Business

```html
<!DOCTYPE html>
<html lang="en">
<head>
<meta charset="utf-8">
<title>Cedar Lantern Letterhead</title>
<link rel="stylesheet" href="https://fonts.googleapis.com/css2?family=Source+Sans+3:wght@400;600&display=swap">
<style>
  :root {
    --backdrop: #e6e6e8;
    --paper: #ededef;
    --leaf-green: #2f6b2a;
    --bark-brown: #6b3414;
    --watermark: #d3d3d5;
  }
  * { margin: 0; padding: 0; box-sizing: border-box; }
  html, body {
    width: 1200px;
    height: 848px;
    overflow: hidden;
    background: var(--backdrop);
    font-family: "Source Sans 3", "Myriad Pro", Arial, sans-serif;
  }
  .letterhead {
    position: absolute;
    left: 290px;
    top: 23px;
    width: 620px;
    height: 802px;
    background: var(--paper);
    box-shadow: 0 1px 4px rgba(0,0,0,0.12);
  }
  .brand {
    position: absolute;
    left: 26px;
    top: 40px;
    display: flex;
    align-items: center;
    gap: 8px;
    color: var(--bark-brown);
    font-weight: 600;
    font-size: 19px;
    letter-spacing: 0.2px;
  }
  .brand-dot {
    width: 14px;
    height: 14px;
    border-radius: 50%;
    background: var(--leaf-green);
  }
  .contact {
    position: absolute;
    right: 26px;
    top: 46px;
    text-align: right;
    color: var(--leaf-green);
    font-size: 10.5px;
    line-height: 13.5px;
    font-style: normal;
  }
  .edge-bar {
    position: absolute;
    right: 0;
    top: 45px;
    width: 10px;
    height: 80px;
    background: var(--bark-brown);
  }
  .watermark {
    position: absolute;
    left: 0;
    right: 0;
    top: 340px;
    text-align: center;
    color: var(--watermark);
    font-weight: 600;
    font-size: 58px;
    letter-spacing: 1px;
  }
  .signature {
    position: absolute;
    left: 0;
    right: 0;
    bottom: 32px;
    text-align: center;
    color: var(--leaf-green);
    font-size: 10px;
    line-height: 12.5px;
  }
  .signature .physician {
    color: var(--bark-brown);
    font-size: 12.5px;
    line-height: 16px;
  }
</style>
</head>
<body>
  <main class="letterhead">
    <div class="brand">
      <span class="brand-dot"></span>
      <span class="brand-name">Cedar Lantern</span>
    </div>

    <address class="contact">
      916-555-0142<br>
      916-555-0143<br>
      2870 Birchwood Lane<br>
      Suite 210<br>
      Alder Falls, CA 95012<br>
      www.cedarlanternhealth.com
    </address>
    <div class="edge-bar"></div>

    <div class="watermark" aria-hidden="true">Cedar Lantern</div>

    <footer class="signature">
      <div class="physician">Marisol Devereaux, MD</div>
      <div>Diplomat, Pacific Board of Psychiatry and Neurology</div>
      <div>Diplomat, Pacific Board of Integrative and Holistic Medicine</div>
    </footer>
  </main>
</body>
</html>
```